Website design for Nutraceutical Contract Manufacturer in NJ

Develop website for a contract manufacturer, specializing in nutraceutical products. Our color theme is based on the colors of the American flag (Pantone blue no. 282 & red no. 193, white), representing a US presence of a company based in Italy. Our website will include a general e-mail box link for additional info. requests, color photos of our operation, a link to our parent company's website, a video, a mission statement, a description of our capabilities.Our internet presence will be on a B2B basis, to include a map of our location and contact information.

Target Market(s)

Businesses seeking contract manufacturer in the US nutraceutical industry.

Industry/Entity Type

Manufacturer

Number of Pages Required

3 page

Font styles to use
Sans Serif

Colors
3176b5
f04a50

Requirements
Must have
• Colors, as described in project description section. Three pages minimum - one to define what we do/location/contact info,/links to affiliated companies, one to showcase certifications, one to provide photos. We are open to having additional pages as suggested, if necessary. Our website for contacts info: www.veltracore-us.com .
• Link to our general email box: info@veltracore-us.com
• Pantone colors detailed in project description.
• HTTPS secure presence
Nice to have
• TBD
Should not have
• PROFANITY

```html
<!DOCTYPE html>
<html lang="en">
<head>
<meta charset="utf-8">
<title>Veltracore US – Nutraceutical Contract Manufacturing</title>
<link href="https://fonts.googleapis.com/css2?family=Nunito:wght@600;700;800&family=Open+Sans:wght@400;600&display=swap" rel="stylesheet">
<style>
:root{
  --red:#c4103f;
  --navy:#0f1f5c;
  --footer:#0b1d57;
  --grey-nav:#ececec;
  --grey-section:#f1f1f1;
  --text:#555a60;
  --dark-bar:#333333;
  --white:#ffffff;
}
*{box-sizing:border-box;margin:0;padding:0}
html,body{width:1200px;height:2936px;overflow:hidden}
body{position:relative;background:var(--white);font-family:"Open Sans",Arial,sans-serif;color:var(--text)}
.abs{position:absolute}
.heading{font-family:"Nunito",Arial,sans-serif;font-weight:800}

/* header */
.site-header{left:0;top:0;width:1200px;height:114px;background:var(--white)}
.brand{left:78px;top:40px;font-family:"Nunito",Arial,sans-serif;font-weight:700;font-size:44px;color:var(--red);letter-spacing:.5px;line-height:1}
.login-btn{left:998px;top:31px;width:123px;height:45px;background:var(--red);color:var(--white);font-family:"Nunito",Arial,sans-serif;font-weight:800;font-size:21px;display:flex;align-items:center;justify-content:center}
.main-nav{left:0;top:114px;width:1200px;height:52px;background:var(--grey-nav)}
.main-nav a{position:absolute;top:0;height:52px;line-height:52px;font-size:16px;color:#555;text-decoration:none;text-transform:uppercase}
.main-nav a.active{color:var(--red);border-bottom:3px solid var(--red)}

/* hero */
.hero{left:0;top:166px;width:1200px;height:564px;background:linear-gradient(180deg,#3c4f86 0%,#56699f 45%,#2f4278 100%)}
.hero-title{left:0;top:374px;width:1200px;text-align:center;font-size:52px;color:var(--white);font-weight:700}
.btn{display:flex;align-items:center;justify-content:center;font-family:"Nunito",Arial,sans-serif;font-weight:800;font-size:21px;text-transform:uppercase}
.btn-light{left:401px;top:472px;width:178px;height:48px;background:var(--white);color:var(--navy)}
.btn-outline{left:599px;top:472px;width:178px;height:48px;border:2px solid var(--white);color:var(--white)}

/* mission */
.section-title{width:1200px;left:0;text-align:center;font-size:40px;color:var(--navy)}
.section-title .accent{color:var(--red)}
.mission-title{top:775px}
.mission-text{left:225px;top:838px;width:750px;text-align:center;font-size:15px;line-height:26px}
.mission-text p+p{margin-top:10px}

/* capabilities */
.cap-block{left:0;top:1039px;width:241px;height:489px;background:var(--red)}
.cap-title{top:1065px}
.video-frame{left:78px;top:1141px;width:490px;height:333px;background:var(--white);padding:10px}
.video-still{width:100%;height:100%;background:linear-gradient(160deg,#8e9aa6 0%,#c5ccd2 45%,#6c7782 100%);display:flex;align-items:center;justify-content:center}
.cap-text{left:636px;top:1180px;width:485px;font-size:15px;line-height:25px}
.cap-text p+p{margin-top:4px}
.btn-navy{left:634px;top:1380px;width:157px;height:39px;background:var(--navy);color:var(--white);font-size:18px}

/* about */
.about{left:0;top:1607px;width:1200px;height:489px;background:var(--grey-section)}
.about-title{top:1650px}
.about-lead{left:0;top:1714px;width:1200px;text-align:center;font-size:15px}
.contacts-title{left:0;top:1762px;width:1200px;text-align:center;font-family:"Nunito",Arial,sans-serif;font-weight:700;font-size:25px;color:#555}
.contact-item{width:360px;font-size:15px;line-height:24px}
.contact-item svg{position:absolute;left:0;top:4px}
.contact-item .txt{padding-left:42px}
.contact-item a,.about-links a{color:var(--text)}
.about-links{left:0;width:1200px;text-align:center;font-size:15px}
.about-links a{color:var(--red)}

/* contact */
.contact-band{left:0;top:2096px;width:1200px;height:489px;background:linear-gradient(120deg,#6f7f9c 0%,#3f5283 40%,#2e3f70 70%,#51628f 100%)}
.contact-title{left:614px;top:2226px;font-size:42px;color:var(--white);font-weight:700}
.field{height:44px;background:rgba(255,255,255,.35);color:#3a3f55;font-size:15px;padding-left:14px;display:flex;align-items:center}
.btn-submit{left:613px;top:2419px;width:164px;height:49px;background:var(--red);color:var(--white)}

/* footer */
.site-footer{left:0;top:2585px;width:1200px;height:292px;background:var(--footer)}
.footer-brand{left:78px;top:2670px;color:var(--white)}
.social{width:50px;height:50px;border:2px solid var(--white);border-radius:50%;display:flex;align-items:center;justify-content:center}
.footer-info{left:815px;font-size:15px;line-height:24px;color:var(--white)}
.footer-info svg{position:absolute;left:0;top:3px}
.footer-info .txt{padding-left:34px}
.copyright{left:0;top:2877px;width:1200px;height:59px;background:var(--dark-bar);color:#e8e8e8;font-size:15px;display:flex;align-items:center;justify-content:center}
</style>
</head>
<body>

<header class="abs site-header">
  <div class="abs brand">Veltracore US</div>
  <div class="abs login-btn">LOGIN</div>
</header>

<nav class="abs main-nav">
  <a class="active" style="left:80px">Home</a>
  <a style="left:176px">What we do</a>
  <a style="left:323px">Locations</a>
  <a style="left:460px">Contact</a>
</nav>

<section class="abs hero" role="img" aria-label="Photo of a clean-room production floor with a conveyor line, operator and stacked cartons"></section>
<h1 class="abs hero-title heading">specializing in nutraceutical products</h1>
<div class="abs btn btn-light">Read more</div>
<div class="abs btn btn-outline">Email us</div>

<h2 class="abs section-title heading mission-title"><span class="accent">Our</span> Mission</h2>
<div class="abs mission-text">
  <p>Lorem Ipsum is simply dummy text of the printing and typesetting industry. Lorem Ipsum has been the industry's standard dummy text ever since the 1500s, when an unknown printer took a galley of type and scrambled it to make a type specimen book.</p>
  <p>It has survived not only five centuries, but also the leap into electronic typesetting, remaining essentially unchanged. It was popularised in the 1960s with the release of Letraset sheets containing.</p>
</div>

<div class="abs cap-block"></div>
<h2 class="abs section-title heading cap-title"><span class="accent">Our</span> Capabilities</h2>
<div class="abs video-frame">
  <div class="video-still" role="img" aria-label="Video still of an automated capsule and tablet packaging machine">
    <svg width="64" height="64" viewBox="0 0 64 64"><circle cx="32" cy="32" r="28" fill="none" stroke="#fff" stroke-width="4"/><path d="M26 20 L45 32 L26 44 Z" fill="#fff"/></svg>
  </div>
</div>
<div class="abs cap-text">
  <p>Lorem Ipsum is simply dummy text of the printing and typesetting industry. Lorem Ipsum has been the industry's standard dummy text ever since the 1500s, when an unknown printer took a galley of type and scrambled it to make a type specimen book.</p>
  <p>Lorem Ipsum is simply dummy text of the printing and typesetting industry. Lorem Ipsum has been the industry's standard dummy text ever since the 1500s, when an unknown printer.</p>
</div>
<div class="abs btn btn-navy">Know more</div>

<section class="abs about"></section>
<h2 class="abs section-title heading about-title"><span class="accent">About</span> Us</h2>
<p class="abs about-lead">Veltracore US LLC is a contract manufacturer for the food supplements market, producing exclusively for third parties.</p>
<h3 class="abs contacts-title">Email Contacts</h3>

<div class="abs contact-item" style="left:233px;top:1818px">
  <svg width="20" height="15" viewBox="0 0 20 15"><rect x="1" y="1" width="18" height="13" fill="none" stroke="#0f1f5c" stroke-width="2"/><path d="M1 1 L10 8 L19 1" fill="none" stroke="#0f1f5c" stroke-width="2"/></svg>
  <div class="txt">President: Marco Ferrante –<br><a>marco.ferrante@veltracore-us.com</a></div>
</div>
<div class="abs contact-item" style="left:624px;top:1818px">
  <svg width="20" height="15" viewBox="0 0 20 15"><rect x="1" y="1" width="18" height="13" fill="none" stroke="#0f1f5c" stroke-width="2"/><path d="M1 1 L10 8 L19 1" fill="none" stroke="#0f1f5c" stroke-width="2"/></svg>
  <div class="txt">Business Manager: Lisa Drummond –<br><a>lisa.drummond@veltracore-us.com</a></div>
</div>
<div class="abs contact-item" style="left:233px;top:1890px">
  <svg width="20" height="15" viewBox="0 0 20 15"><rect x="1" y="1" width="18" height="13" fill="none" stroke="#0f1f5c" stroke-width="2"/><path d="M1 1 L10 8 L19 1" fill="none" stroke="#0f1f5c" stroke-width="2"/></svg>
  <div class="txt">Quality Assurance: Paolo Renzi –<br><a>paolo.renzi@veltracore-us.com</a></div>
</div>
<div class="abs contact-item" style="left:624px;top:1890px">
  <svg width="20" height="15" viewBox="0 0 20 15"><rect x="1" y="1" width="18" height="13" fill="none" stroke="#0f1f5c" stroke-width="2"/><path d="M1 1 L10 8 L19 1" fill="none" stroke="#0f1f5c" stroke-width="2"/></svg>
  <div class="txt">Member: Kevin Ashford –<br><a>kevin.ashford@veltracore-us.com</a></div>
</div>

<p class="abs about-links" style="top:1978px">visit our parent company's website : <a>www.veltracore-us.com</a></p>
<p class="abs about-links" style="top:2014px">view our certificates : <a>www.veltracore-us.com</a></p>

<section class="abs contact-band" role="img" aria-label="Dusk photo of the company building and roadside sign in winter snow, with blue overlay"></section>
<h2 class="abs contact-title heading">Contact Us</h2>
<div class="abs field" style="left:613px;top:2300px;width:248px">Name</div>
<div class="abs field" style="left:875px;top:2300px;width:246px">Email</div>
<div class="abs field" style="left:613px;top:2356px;width:508px">Subject</div>
<div class="abs btn btn-submit">Submit</div>

<footer class="abs site-footer"></footer>
<div class="abs brand footer-brand">Veltracore US</div>
<div class="abs social" style="left:77px;top:2758px"></div>
<div class="abs social" style="left:145px;top:2758px"></div>
<div class="abs social" style="left:214px;top:2758px"></div>
<div class="abs social" style="left:282px;top:2758px">
  <svg width="22" height="16" viewBox="0 0 22 16"><rect x="0" y="0" width="22" height="16" rx="2" fill="#fff"/><path d="M1 1 L11 9 L21 1" fill="none" stroke="#0b1d57" stroke-width="2"/></svg>
</div>

<div class="abs footer-info" style="top:2646px">
  <svg width="18" height="22" viewBox="0 0 18 22"><path d="M9 0 C4 0 0 4 0 9 C0 15 9 22 9 22 C9 22 18 15 18 9 C18 4 14 0 9 0 Z" fill="#fff"/><circle cx="9" cy="9" r="3.5" fill="#0b1d57"/></svg>
  <div class="txt">210 Orchard Way<br>Millbrook, NJ 08500 USA</div>
</div>
<div class="abs footer-info" style="top:2710px">
  <svg width="18" height="18" viewBox="0 0 18 18"><path d="M4 0 L7 5 L5 7 C6 10 8 12 11 13 L13 11 L18 14 L16 18 C8 18 0 10 0 2 Z" fill="#fff"/></svg>
  <div class="txt">+1 (609) 555-0146</div>
</div>
<div class="abs footer-info" style="top:2753px">
  <svg width="18" height="18" viewBox="0 0 18 18"><rect x="0" y="5" width="18" height="13" rx="1" fill="#fff"/><rect x="4" y="0" width="10" height="6" fill="#fff"/><rect x="3" y="8" width="6" height="3" fill="#0b1d57"/><rect x="11" y="8" width="4" height="2" fill="#0b1d57"/><rect x="11" y="12" width="4" height="2" fill="#0b1d57"/></svg>
  <div class="txt">+1 (609) 555-0162</div>
</div>
<div class="abs footer-info" style="top:2790px">
  <svg width="20" height="15" viewBox="0 0 20 15"><rect x="1" y="1" width="18" height="13" fill="none" stroke="#fff" stroke-width="2"/><path d="M1 1 L10 8 L19 1" fill="none" stroke="#fff" stroke-width="2"/></svg>
  <div class="txt">info@veltracore-us.com</div>
</div>

<div class="abs copyright">©Veltracore US. 2018 - All Rights Reserved.</div>

</body>
</html>
```